Create Brisk Lesson Studio a card design that will stick in the mind of prospects.

Brisk Lesson Studio specialises designs and produces training video, animation, illustration and text.

We need a card design that oozes class and leaves the prospect brimming with confidence.

The design will feature the Brisk Lesson Studio all black logo (uploaded). The design may also use the shade of orange from the orange version of the logo (uploaded). Note, just the color is to be used e.g. for the back of the card, not the orange logo itself.

The Brisk brand is about authenticity, quality, maturity and assurance. We are a safe buy when it comes to the prospects next project.

Target Market(s)

The primary target is training managers or others who are responsible for choosing to hire companies to produce their training media e.g. video. This will usually be a large spend so they need to have confidence.

Industry/Entity Type

Training

Contact Information for Business Card

FRONT:

Brisk Lesson Studio
Phone: 03 5172 4039
1st Floor, 418 Kellerby Road
Mt Ferncombe
VIC 3862
Australia
www.brisklesson.com.au

Lionel Petch
Founder and Lead Consultant
mobile: +61 3 0462 735 218
email: lionel@brisklesson.com.au

BACK:
Specialising in design and production of training:

video
animation
illustration
text

for delivery via internet, intranet and/or LMS.

Number of Pages Required

4 page

Font styles to use
Sans Serif

Requirements
Must have
• The black logo uploaded with the brief.
Nice to have
• The inclusion of the shade of orange found in the orange logo also uploaded with the brief. One example would be having the back of the card in this orange and using a white font for the text. But I want the designer to work this out.
Should not have
• No colours other than black and the orange included in the uploaded orange logo.

```html
<!DOCTYPE html>
<html lang="en">
<head>
<meta charset="utf-8">
<title>Brisk Lesson Studio – Business Card</title>
<link rel="stylesheet" href="https://fonts.googleapis.com/css2?family=Arimo:wght@400;700&display=swap">
<style>
  :root {
    --orange: #e57718;
    --black: #231f20;
    --white: #ffffff;
    --backdrop: #d9d9d9;
    --rule: rgba(35, 31, 32, 0.55);
  }
  * { box-sizing: border-box; margin: 0; padding: 0; }
  html, body {
    width: 1200px; height: 1200px; overflow: hidden;
    background: var(--backdrop);
    font-family: "Arimo", Arial, sans-serif;
  }
  .canvas { position: relative; width: 1200px; height: 1200px; }
  .card {
    position: absolute; left: 237px; width: 722px; height: 441px;
    overflow: hidden;
    box-shadow: 0 14px 22px rgba(0,0,0,0.28);
  }
  .card--front { top: 101px; background: var(--orange); }
  .card--back { top: 624px; background: var(--white); }

  /* front */
  .front__brand-panel {
    position: absolute; left: 0; top: 0; width: 403px; height: 100%;
    background: var(--black);
  }
  .brand-mark {
    position: absolute; left: 0; width: 100%; text-align: center;
    color: var(--orange); font-weight: 700; letter-spacing: -1px;
  }
  .front__brand-panel .brand-mark { top: 152px; font-size: 72px; }
  .front__company {
    position: absolute; left: 0; top: 300px; width: 100%; text-align: center;
    color: var(--white); font-weight: 700; font-size: 24px; letter-spacing: 0.2px;
  }
  .front__person { position: absolute; left: 438px; top: 46px; color: var(--black); }
  .person__name { font-weight: 700; font-size: 29px; letter-spacing: 0.4px; text-transform: uppercase; }
  .person__title { font-size: 15px; margin-top: 4px; }
  .contact-rail {
    position: absolute; left: 407px; top: 184px; width: 46px; bottom: 0;
    background: var(--black);
  }
  .contact-list { position: absolute; left: 425px; top: 196px; list-style: none; }
  .contact-item {
    position: relative; display: flex; align-items: center;
    width: 287px; height: 43px;
    border-bottom: 1px solid var(--rule);
    color: var(--white); font-size: 14px; line-height: 1.2;
  }
  .contact-item--address { height: 51px; }
  .contact-item__icon {
    flex: none; width: 38px; height: 38px; margin-right: 12px;
    background: var(--orange); border-radius: 19px 0 0 19px;
    display: flex; align-items: center; justify-content: center;
  }
  .contact-item__icon svg { width: 20px; height: 20px; fill: var(--white); }

  /* back */
  .card--back .brand-mark { top: 96px; font-size: 84px; }
  .back__company {
    position: absolute; left: 0; top: 272px; width: 100%; text-align: center;
    color: var(--black); font-weight: 700; font-size: 30px; letter-spacing: 0.3px;
  }
  .back__band {
    position: absolute; left: 0; top: 324px; width: 100%; height: 117px;
    background: var(--orange); color: var(--white); text-align: center; font-size: 13px;
  }
  .band__intro { margin-top: 16px; }
  .service-pill {
    display: inline-flex; margin-top: 6px; height: 26px; align-items: center;
    background: var(--black); border-radius: 13px; padding: 0 22px;
    list-style: none;
  }
  .service-pill li { padding: 0 12px; border-left: 1px solid var(--white); line-height: 18px; }
  .service-pill li:first-child { border-left: none; }
  .band__outro { margin-top: 7px; }
</style>
</head>
<body>
<main class="canvas">
  <section class="card card--front" aria-label="Card front">
    <div class="front__brand-panel">
      <div class="brand-mark">Brisk</div>
      <div class="front__company">BRISK LESSON STUDIO</div>
    </div>
    <div class="front__person">
      <div class="person__name">Lionel Petch</div>
      <div class="person__title">Founder and Lead Consultant</div>
    </div>
    <div class="contact-rail"></div>
    <ul class="contact-list">
      <li class="contact-item contact-item--address">
        <span class="contact-item__icon"><svg viewBox="0 0 20 20"><path d="M10 3 2 10h2.5v7h4v-5h3v5h4v-7H18z"/></svg></span>
        <span>1st Floor, 418 Kellerby Road,<br>Mt Ferncombe, VIC 3862, Australia</span>
      </li>
      <li class="contact-item">
        <span class="contact-item__icon"><svg viewBox="0 0 20 20"><path d="M2 7c0-2 3-3 8-3s8 1 8 3v1.5h-4V7H6v1.5H2zM5 10h10l2 6H3z"/></svg></span>
        <span>03 5172 4039</span>
      </li>
      <li class="contact-item">
        <span class="contact-item__icon"><svg viewBox="0 0 20 20"><path d="M7 2h6a1 1 0 0 1 1 1v14a1 1 0 0 1-1 1H7a1 1 0 0 1-1-1V3a1 1 0 0 1 1-1zm1 2v7h4V4z"/></svg></span>
        <span>+61 3 0462 735 218</span>
      </li>
      <li class="contact-item">
        <span class="contact-item__icon"><svg viewBox="0 0 20 20"><text x="10" y="15.5" text-anchor="middle" font-size="17" font-family="Arimo, sans-serif" font-weight="700" fill="#fff">@</text></svg></span>
        <span>lionel@brisklesson.com.au</span>
      </li>
      <li class="contact-item">
        <span class="contact-item__icon"><svg viewBox="0 0 20 20"><path d="M3 3h14v10H3zm2 2v6h10V5zM1 15h18v2H1z"/></svg></span>
        <span>www.brisklesson.com.au</span>
      </li>
    </ul>
  </section>

  <section class="card card--back" aria-label="Card back">
    <div class="brand-mark">Brisk</div>
    <div class="back__company">BRISK LESSON STUDIO</div>
    <div class="back__band">
      <p class="band__intro">Specialising in design and production of training:</p>
      <ul class="service-pill">
        <li>video</li><li>animation</li><li>illustration</li><li>text</li>
      </ul>
      <p class="band__outro">for delivery via internet, intranet and/or LMS.</p>
    </div>
  </section>
</main>
</body>
</html>
```